Prestige Car Bodyshop Business Card

We are a car bodyshop based in the UK. Our customer base is mainly prestige high-value vehicles. I am looking for a classy and stylish business card design for my staff to give out to customers, with their direct email and phone number, as well as our main email and phone number with address details

I am also looking to have a general business card design with just our main company address and contact details, but also have a space to add a manufacturer approval logo (i.e Velmora, Orek, Tovalo etc... logo) in the corner somewhere.

I do not particularly want any outlines or pictures of cars on the card, I would just like a quality high-end look.

Please feel free to get in touch if you have any questions or queries?

Many Thanks

Malcolm

Target Market(s)

Prestige vehicle owners

Industry/Entity Type

Automotive

Contact Information for Business Card

I am looking for a classy and stylish business card design for my staff to give out to customers, with their direct email and phone number, as well as our main email and phone number with address details

Font styles to use
Sans Serif

Colors

Designer to choose colors to be used in the design.

Requirements
Nice to have
• I do not particularly want any outlines or pictures of cars on the card, I would just like a quality high-end look.

```html
<!DOCTYPE html>
<html lang="en">
<head>
<meta charset="utf-8">
<title>Halden Accident Repair Centre – Business Cards</title>
<link rel="stylesheet" href="https://fonts.googleapis.com/css2?family=Open+Sans:wght@300;400;600&display=swap">
<style>
  :root {
    --backdrop: #1c1c1e;
    --card: #13203a;
    --card-edge: #0d1729;
    --mark: #2a5aa8;
    --accent: #1f9de3;
    --text: #f2f4f8;
    --text-soft: #c9d2e0;
  }
  * { box-sizing: border-box; margin: 0; padding: 0; }
  html, body { width: 1200px; height: 900px; overflow: hidden; }
  body {
    background: var(--backdrop);
    font-family: "Open Sans", Arial, sans-serif;
    color: var(--text);
    position: relative;
  }
  .card {
    position: absolute;
    width: 540px;
    height: 310px;
    background: var(--card);
    border-radius: 4px;
    box-shadow: 0 0 0 1px var(--card-edge);
    overflow: hidden;
  }
  .card--back  { left: 50px;  top: 295px; }
  .card--front { left: 610px; top: 295px; }

  .brand { position: absolute; display: flex; align-items: center; gap: 14px; }
  .brand__dot { border-radius: 50%; background: var(--mark); flex: none; }
  .brand__text { display: flex; flex-direction: column; }
  .brand__name {
    font-weight: 300; letter-spacing: 2px; color: var(--text);
    border-bottom: 1px solid var(--text); line-height: 1.1;
  }
  .brand__tagline { font-weight: 300; letter-spacing: 1px; color: var(--text); text-transform: uppercase; margin-top: 4px; }

  .card--back .brand { left: 40px; top: 40px; }
  .card--back .brand__dot { width: 60px; height: 60px; }
  .card--back .brand__name { font-size: 30px; padding-bottom: 4px; }
  .card--back .brand__tagline { font-size: 10px; }

  .card--front .brand { left: 120px; top: 90px; }
  .card--front .brand__dot { width: 80px; height: 80px; }
  .card--front .brand__name { font-size: 40px; padding-bottom: 6px; }
  .card--front .brand__tagline { font-size: 12px; }
  .front__web { position: absolute; left: 120px; top: 200px; font-size: 15px; letter-spacing: 0.5px; }

  .person { position: absolute; right: 70px; top: 150px; }
  .person__name { color: var(--accent); font-size: 17px; font-weight: 400; }
  .person__title { color: var(--text-soft); font-size: 10px; font-weight: 600; }

  .contacts {
    position: absolute; left: 30px; right: 30px; bottom: 36px;
    display: flex; align-items: center;
  }
  .contact { display: flex; align-items: center; gap: 7px; font-size: 15px; white-space: nowrap; }
  .contact svg { width: 13px; height: 13px; flex: none; }
  .contact__divider {
    width: 1px; height: 52px; margin: 0 20px;
    background: linear-gradient(to bottom, transparent, var(--accent), transparent);
  }
</style>
</head>
<body>
  <section class="card card--back" aria-label="Business card, contact side">
    <div class="brand">
      <span class="brand__dot"></span>
      <div class="brand__text">
        <span class="brand__name">HALDEN</span>
        <span class="brand__tagline">Accident Repair Centre</span>
      </div>
    </div>

    <div class="person">
      <p class="person__name">Malcolm</p>
      <p class="person__title">Title</p>
    </div>

    <div class="contacts">
      <div class="contact">
        <svg viewBox="0 0 16 16" aria-hidden="true"><path fill="#1f9de3" d="M3.5 1l2.5 3-1.5 2c1 2 3 4 5 5l2-1.5 3 2.5-1.5 2.5C7 14 2 9 1 2.5z"/></svg>
        <span>0117 555 0142</span>
      </div>
      <span class="contact__divider"></span>
      <div class="contact">
        <svg viewBox="0 0 16 16" aria-hidden="true"><g fill="none" stroke="#1f9de3" stroke-width="1.3"><circle cx="8" cy="8" r="6.5"/><ellipse cx="8" cy="8" rx="3" ry="6.5"/><path d="M1.5 8h13M2.5 4.5h11M2.5 11.5h11"/></g></svg>
        <span>www.halden.co.uk</span>
      </div>
      <span class="contact__divider"></span>
      <div class="contact">
        <svg viewBox="0 0 16 16" aria-hidden="true"><g fill="none" stroke="#1f9de3" stroke-width="1.3"><rect x="1.5" y="3.5" width="13" height="9"/><path d="M1.5 3.5l6.5 5.5 6.5-5.5"/></g></svg>
        <span>info@halden.co.uk</span>
      </div>
    </div>
  </section>

  <section class="card card--front" aria-label="Business card, front side">
    <div class="brand">
      <span class="brand__dot"></span>
      <div class="brand__text">
        <span class="brand__name">HALDEN</span>
        <span class="brand__tagline">Accident Repair Centre</span>
      </div>
    </div>
    <p class="front__web">www.halden.co.uk</p>
  </section>
</body>
</html>
```